Harrowmere Sack operates across the US and Australasia providing calico bags to small business through to large enterprise across all verticals. Our bags are the most premium in the market place and our customer service is second to none. Our competitive advantage lays in our competitive pricing, superior quality and outstanding customer service.

Industry/Entity Type

Business

Contact Information for Business Card

Harrowmere Sack
Delphine Marrow
Managing Director
delphine@harrowmeresack.com
www.harrowmeresack.com.au
Mobile:- 0417 689 305
Level 3, 248 Pembury Street
Melbourne Victoria Australia 3008

```html
<!DOCTYPE html>
<html lang="en">
<head>
<meta charset="utf-8">
<title>Harrowmere Sack – Business Card</title>
<link rel="stylesheet" href="https://fonts.googleapis.com/css2?family=Tinos:wght@400;700&display=swap">
<style>
  :root {
    --backdrop: #2b2725;
    --card: #151515;
    --card-edge: #262626;
    --brand-green: #5fb31f;
    --brand-green-light: #8fd64a;
    --ink-light: #f2f2f2;
    --ink-muted: #d6d6d6;
    --divider: #8a8a8a;
  }
  * { box-sizing: border-box; margin: 0; padding: 0; }
  html, body {
    width: 1200px;
    height: 780px;
    overflow: hidden;
    background: var(--backdrop);
    font-family: "Tinos", "Times New Roman", serif;
  }
  .sheet {
    width: 1200px;
    height: 780px;
    display: flex;
    align-items: center;
    justify-content: center;
    gap: 60px;
  }
  .card {
    width: 540px;
    height: 310px;
    background: var(--card);
    border: 1px solid var(--card-edge);
    border-radius: 4px;
    box-shadow: 0 14px 30px rgba(0,0,0,0.45);
    position: relative;
    overflow: hidden;
  }
  /* Front */
  .card-front {
    display: flex;
    align-items: center;
    padding: 0 34px;
  }
  .brand-block {
    width: 190px;
    display: flex;
    align-items: center;
    gap: 10px;
  }
  .brand-dot {
    width: 22px;
    height: 22px;
    border-radius: 50%;
    background: var(--brand-green);
    flex: none;
  }
  .brand-name {
    color: var(--brand-green);
    font-weight: 700;
    font-size: 22px;
    line-height: 1.1;
  }
  .divider {
    width: 1px;
    height: 200px;
    background: var(--divider);
    margin: 0 30px 0 16px;
  }
  .details { flex: 1; }
  .person-name {
    color: var(--brand-green);
    font-size: 28px;
    line-height: 1;
  }
  .person-role {
    color: var(--ink-light);
    font-size: 15px;
    margin-top: 4px;
  }
  .contact-list {
    list-style: none;
    margin-top: 34px;
  }
  .contact-item {
    display: flex;
    align-items: center;
    gap: 9px;
    color: var(--ink-light);
    font-size: 14px;
    line-height: 1.45;
  }
  .contact-icon {
    width: 12px;
    height: 12px;
    flex: none;
  }
  .contact-address { padding-left: 21px; color: var(--ink-muted); }
  /* Back */
  .card-back {
    display: flex;
    align-items: center;
    justify-content: center;
    gap: 14px;
  }
  .card-back .brand-dot { width: 40px; height: 40px; }
  .card-back .brand-name { font-size: 40px; }
</style>
</head>
<body>
<main class="sheet">
  <section class="card card-front" aria-label="Business card front">
    <div class="brand-block">
      <span class="brand-dot" aria-hidden="true"></span>
      <span class="brand-name">Harrowmere Sack</span>
    </div>
    <div class="divider" aria-hidden="true"></div>
    <div class="details">
      <h1 class="person-name">Delphine Marrow</h1>
      <p class="person-role">Managing Director</p>
      <ul class="contact-list">
        <li class="contact-item">
          <svg class="contact-icon" viewBox="0 0 12 12" aria-hidden="true"><rect width="12" height="12" rx="1.5" fill="var(--brand-green)"/><path d="M3.5 2.5h2l.6 2-1 .8a5 5 0 0 0 1.6 1.6l.8-1 2 .6v2a1 1 0 0 1-1 1A6 6 0 0 1 2.5 3.5a1 1 0 0 1 1-1z" fill="#151515"/></svg>
          0417 689 305
        </li>
        <li class="contact-item">
          <svg class="contact-icon" viewBox="0 0 12 12" aria-hidden="true"><rect width="12" height="12" rx="1.5" fill="var(--brand-green)"/><circle cx="6" cy="6" r="3.3" fill="none" stroke="#151515" stroke-width="1"/><path d="M2.7 6h6.6M6 2.7v6.6" stroke="#151515" stroke-width="0.8"/></svg>
          www.harrowmeresack.com.au
        </li>
        <li class="contact-item">
          <svg class="contact-icon" viewBox="0 0 12 12" aria-hidden="true"><rect width="12" height="12" rx="1.5" fill="var(--brand-green)"/><rect x="2.5" y="3.5" width="7" height="5" fill="none" stroke="#151515" stroke-width="1"/><path d="M2.5 3.5L6 6.3l3.5-2.8" fill="none" stroke="#151515" stroke-width="1"/></svg>
          delphine@harrowmeresack.com
        </li>
        <li class="contact-item">
          <svg class="contact-icon" viewBox="0 0 12 12" aria-hidden="true"><rect width="12" height="12" rx="1.5" fill="var(--brand-green)"/><path d="M6 10S3 6.8 3 4.8a3 3 0 0 1 6 0C9 6.8 6 10 6 10z" fill="#151515"/><circle cx="6" cy="4.8" r="1" fill="var(--brand-green)"/></svg>
          Level 3, 248 Pembury Street
        </li>
        <li class="contact-item contact-address">Melbourne Victoria Australia 3008</li>
      </ul>
    </div>
  </section>

  <section class="card card-back" aria-label="Business card back">
    <span class="brand-dot" aria-hidden="true"></span>
    <span class="brand-name">Harrowmere Sack</span>
  </section>
</main>
</body>
</html>
```